Malcolm Tasker Engineering (MTE)

We require a design so that we can start to incorporate the design into our branding

Our core business is Railway Bridges, Road Bridges, Civil Engineering

We require something vibrant & related to our core business.

We have been in business for 30 years and still operate on plain black & white letter heads & business cards. We urgently require a Logo - Brand

Industry/Entity Type

Business

Contact Information for Business Card

Vibrant

Logo Text

Open to options

Font styles to use
Serif

```html
<!DOCTYPE html>
<html lang="en">
<head>
<meta charset="utf-8">
<title>Malcolm Tasker Engineering — Business Card</title>
<link rel="stylesheet" href="https://fonts.googleapis.com/css2?family=Tinos:wght@400;700&display=swap">
<style>
  :root {
    --navy: #1f4a6b;
    --navy-deep: #122f47;
    --navy-panel: #24527a;
    --paper: #ffffff;
    --paper-shade: #e9ecef;
    --backdrop: #e6e6e8;
    --ink-light: #ffffff;
  }
  * { box-sizing: border-box; margin: 0; padding: 0; }
  html, body {
    width: 1200px; height: 800px; overflow: hidden;
    background: var(--backdrop);
    font-family: "Tinos", "Times New Roman", serif;
  }
  .canvas { position: relative; width: 1200px; height: 800px; }

  .card {
    position: absolute;
    width: 540px; height: 310px;
    overflow: hidden;
    background: var(--navy);
    box-shadow: 0 6px 18px rgba(0,0,0,.18);
  }
  .card--front { left: 50px; top: 90px; }
  .card--back  { left: 610px; top: 400px; }

  /* Front */
  .front-panel {
    position: absolute; left: 0; top: 0;
    width: 448px; height: 250px;
    background: linear-gradient(180deg, var(--paper) 70%, var(--paper-shade));
    border-bottom-right-radius: 44px;
    box-shadow: 4px 6px 12px rgba(0,0,0,.35);
    display: flex; align-items: center; justify-content: center;
  }

  .wordmark { text-align: center; color: var(--navy); font-weight: 700; line-height: 1; }
  .wordmark__name { display: block; font-size: 44px; letter-spacing: -0.5px; }
  .wordmark__sub  { display: block; font-size: 22px; letter-spacing: 9px; margin-top: 8px; }
  .wordmark--light { color: var(--ink-light); }
  .wordmark--light .wordmark__name { font-size: 30px; }
  .wordmark--light .wordmark__sub  { font-size: 15px; letter-spacing: 6px; margin-top: 6px; }

  /* Back */
  .back-logo {
    position: absolute; left: 0; top: 0;
    width: 335px; height: 310px;
    display: flex; align-items: center; justify-content: center;
    padding-top: 60px;
  }
  .contact-panel {
    position: absolute; left: 335px; top: 0;
    width: 205px; height: 310px;
    background: linear-gradient(90deg, var(--navy-panel), var(--navy));
    box-shadow: -6px 0 14px rgba(0,0,0,.25);
  }
  .name-ribbon {
    position: absolute; left: 322px; top: 70px;
    width: 218px; height: 52px;
    background: var(--navy-deep);
    color: var(--ink-light);
    padding: 8px 0 0 20px;
    box-shadow: 0 4px 8px rgba(0,0,0,.35);
  }
  .name-ribbon__name  { font-size: 20px; font-weight: 700; line-height: 1.05; }
  .name-ribbon__title { font-size: 11px; }

  .contact-list {
    position: absolute; left: 348px; top: 138px;
    list-style: none; color: var(--ink-light);
    font-size: 13.5px; line-height: 1.2;
  }
  .contact-list li { display: flex; align-items: flex-start; gap: 10px; margin-bottom: 8px; }
  .contact-list svg { flex: none; width: 16px; height: 16px; fill: var(--ink-light); }
</style>
</head>
<body>
<main class="canvas">

  <section class="card card--front" aria-label="Business card front">
    <div class="front-panel">
      <div class="wordmark">
        <span class="wordmark__name">Malcolm Tasker</span>
        <span class="wordmark__sub">ENGINEERING</span>
      </div>
    </div>
  </section>

  <section class="card card--back" aria-label="Business card back">
    <div class="back-logo">
      <div class="wordmark wordmark--light">
        <span class="wordmark__name">Malcolm Tasker</span>
        <span class="wordmark__sub">ENGINEERING</span>
      </div>
    </div>

    <div class="contact-panel"></div>

    <div class="name-ribbon">
      <div class="name-ribbon__name">Owen Hartley</div>
      <div class="name-ribbon__title">Marketing Director</div>
    </div>

    <ul class="contact-list">
      <li>
        <svg viewBox="0 0 16 16" aria-hidden="true"><path d="M3 1h3l1 4-2 1c1 2 3 4 5 5l1-2 4 1v3c0 1-1 2-2 2C7 15 1 9 1 3c0-1 1-2 2-2z"/></svg>
        <span>123 123 1234</span>
      </li>
      <li>
        <svg viewBox="0 0 16 16" aria-hidden="true"><path d="M4 0h8a1 1 0 0 1 1 1v14a1 1 0 0 1-1 1H4a1 1 0 0 1-1-1V1a1 1 0 0 1 1-1zm1 2v10h6V2zm3 11a1 1 0 1 0 0 2 1 1 0 0 0 0-2z"/></svg>
        <span>123 123 1234</span>
      </li>
      <li>
        <svg viewBox="0 0 16 16" aria-hidden="true"><path d="M1 3h14v10H1zm1.5 1.2V12h11V4.2L8 9zM3 4l5 4 5-4z"/></svg>
        <span>email@email.com</span>
      </li>
      <li>
        <svg viewBox="0 0 16 16" aria-hidden="true"><rect x="1" y="1" width="14" height="14" rx="2"/></svg>
        <span>linkpage.net/MTE</span>
      </li>
      <li>
        <svg viewBox="0 0 16 16" aria-hidden="true"><path d="M8 0a5.5 5.5 0 0 1 5.5 5.5C13.5 10 8 16 8 16S2.5 10 2.5 5.5A5.5 5.5 0 0 1 8 0zm0 3.5a2 2 0 1 0 0 4 2 2 0 0 0 0-4z"/></svg>
        <span>1234 Pretend Rd<br>Pretend City PC 12345</span>
      </li>
    </ul>
  </section>

</main>
</body>
</html>
```